Co-living

We are starting a new co-living company, where people rent rooms only and share kitchen, living, and common areas. Check this website to get an idea of what we want. http://brixlane.io/

Target Market(s)

Single people between 18-30 years old.

Industry/Entity Type

Property Management

Number of Pages Required

5+ page

Font styles to use
Serif

Colors

Designer to choose colors to be used in the design.

Requirements
Must have
• Check this website. We also want a drop menu under "properties" for all of our homes.
• http://brixlane.io/
Nice to have
• a intro video like in this page
• http://brixlane.io/
Should not have
• too much content words, etc.

```html
<!DOCTYPE html>
<html lang="en">
<head>
<meta charset="utf-8">
<title>Hearthside — Co-Living Spaces</title>
<link href="https://fonts.googleapis.com/css2?family=Rajdhani:wght@300;500;600;700&family=Lato:wght@400;700&display=swap" rel="stylesheet">
<style>
:root{
  --blue:#0a5aa3;
  --blue-dark:#084a87;
  --ink:#1b1b1b;
  --grey-badge:#4a4a4a;
  --text:#5f5f5f;
  --panel:#eeeeee;
  --white:#ffffff;
  --head:"Rajdhani",sans-serif;
  --body:"Lato",sans-serif;
}
*{margin:0;padding:0;box-sizing:border-box}
html,body{width:1200px;height:4501px;overflow:hidden;background:var(--white)}
body{position:relative;font-family:var(--body);color:var(--ink)}
.abs{position:absolute}
.hero-art{position:absolute;left:0;top:0}
.nav-logo{left:166px;top:14px;width:210px;height:42px;border:2px solid var(--blue);color:var(--blue);font:500 28px/38px var(--head);text-align:center;letter-spacing:1px}
.nav-line{left:166px;top:70px;width:872px;height:1px;background:rgba(255,255,255,.35)}
.nav-link{top:26px;color:#fff;font:700 12px/16px var(--body)}
.btn{position:absolute;background:var(--blue);color:#fff;font:700 16px var(--head);display:flex;align-items:center;justify-content:center;letter-spacing:.3px}
.btn-outline{background:#fff;color:var(--blue);border:1.5px solid var(--blue);font-weight:500}
.btn-white{background:#fff;color:var(--blue-dark)}
.hero-badge{left:487px;top:280px;width:226px;height:45px;background:rgba(10,50,90,.55);border:2px solid var(--blue);color:#fff;font:600 24px/41px var(--head);text-align:center}
.hero-title{left:0;width:1200px;top:342px;text-align:center;color:#fff;font:700 74px/84px var(--head);letter-spacing:1px}
.badge{position:absolute;background:var(--grey-badge);color:#fff;font:700 10px/28px var(--body);padding:0 14px;height:28px;white-space:nowrap}
.badge.center{transform:translateX(-50%)}
.badge.light{background:#fff;color:#444;font-weight:400}
.h2{position:absolute;font:700 40px/46px var(--head);color:var(--ink)}
.h2.center{left:0;width:1200px;text-align:center}
.copy{position:absolute;font:400 11px/19.5px var(--body);color:var(--text)}
.card{position:absolute;width:278px;height:269px}
.card .photo{height:210px}
.card .label{height:59px;background:var(--blue);color:#fff;text-align:center;padding-top:13px}
.card .label b{display:block;font:700 15px/18px var(--body)}
.card .label span{font:400 11px/15px var(--body)}
.partners{left:0;top:2046px;width:1200px;height:524px;background:var(--panel)}
.p-card{position:absolute;top:2245px;width:428px;height:178px;background:#fff;text-align:center;padding-top:47px}
.p-card h3{font:700 16px/20px var(--body);color:var(--ink)}
.p-card p{font:400 11px/19.5px var(--body);color:var(--text);padding:8px 16px 0}
.band{left:0;top:2570px;width:1200px;height:323px;background:var(--blue)}
.band-title{left:0;width:1200px;top:2654px;text-align:center;color:#fff;font:300 42px/48px var(--head)}
.band-copy{left:300px;width:600px;top:2702px;text-align:center;color:#e3edf7;font:400 11px/19.5px var(--body)}
.tile{position:absolute;width:203px;height:203px}
.press{position:absolute;top:4098px;width:158px;height:96px;border:1px solid #d8d8d8;display:flex;align-items:center;justify-content:center}
.press i{display:block;width:96px;height:30px;border-radius:4px;background:#d5d9de}
.dot{position:absolute;top:4211px;width:8px;height:8px;border-radius:50%;background:#d8d8d8}
.footer{left:0;top:4252px;width:1200px;height:249px;background:var(--blue);overflow:hidden}
.foot-logo{left:496px;top:28px;width:210px;height:42px;border:2px solid #fff;color:#fff;font:500 28px/38px var(--head);text-align:center;letter-spacing:1px}
.foot-link{top:95px;color:#fff;font:400 14px/18px var(--body)}
.social{top:140px;width:30px;height:30px;border-radius:50%;background:#fff;opacity:.92}
.legal{left:0;width:1200px;top:198px;text-align:center;color:#dbe6f2;font:400 11px/14px var(--body)}
</style>
</head>
<body>

<!-- HERO -->
<svg class="hero-art" width="1200" height="800" viewBox="0 0 1200 800">
  <defs>
    <linearGradient id="heroGrad" x1="0" y1="0" x2="1" y2="1">
      <stop offset="0" stop-color="#1b1e24"/>
      <stop offset=".45" stop-color="#34302a"/>
      <stop offset=".75" stop-color="#4a3f2c"/>
      <stop offset="1" stop-color="#232324"/>
    </linearGradient>
  </defs>
  <path role="img" aria-label="Photo of young housemates laughing together in a shared lounge" fill="url(#heroGrad)"
    d="M0 0H1200V475C1168 490 1150 530 1140 590C1118 700 1010 722 900 703C780 684 700 690 600 700C460 716 380 780 250 772C140 765 50 700 0 590Z"/>
  <circle cx="600" cy="229" r="24" fill="none" stroke="#fff" stroke-width="3"/>
  <path d="M592 216L612 229L592 242Z" fill="#fff"/>
</svg>

<header>
  <div class="abs nav-logo">HEARTHSIDE</div>
  <nav>
    <span class="abs nav-link" style="left:638px">Properties <svg width="12" height="8" viewBox="0 0 12 8"><path d="M1 1L6 6L11 1Z" fill="#3d8ee0"/></svg></span>
    <span class="abs nav-link" style="left:756px">About Us</span>
    <span class="abs nav-link" style="left:852px">Partner</span>
  </nav>
  <a class="btn" style="left:948px;top:17px;width:90px;height:35px;font:700 12px var(--body)">Join Now</a>
  <div class="abs nav-line"></div>
</header>

<div class="abs hero-badge">Co- Living Spaces</div>
<h1 class="abs hero-title">LIVE BETTER TOGETHER</h1>
<a class="btn" style="left:526px;top:454px;width:148px;height:51px;font-size:18px">Contact Us</a>

<!-- ABOUT -->
<section>
  <span class="badge" style="left:161px;top:826px">Co-Living Spaces</span>
  <h2 class="h2" style="left:161px;top:862px">About Co-Living</h2>
  <p class="copy" style="left:161px;top:926px;width:428px">Lorem Ipsum is simply dummy text of the printing and typesetting industry. Lorem Ipsum has been the industry's standard dummy text ever since the 1500s, when an unknown printer took a galley of type and scrambled it to make a type specimen book.</p>
  <p class="copy" style="left:161px;top:1026px;width:428px">&nbsp;It was popularised in the 1960s with the release of transfer sheets containing Lorem Ipsum passages, and more recently with desktop publishing software and page layout tools including versions of Lorem Ipsum.</p>
  <a class="btn" style="left:161px;top:1127px;width:113px;height:35px;font-size:15px">Find Your's</a>

  <svg class="abs" style="left:600px;top:730px" width="520" height="450" viewBox="600 730 520 450">
    <defs>
      <linearGradient id="ring" x1="0" y1="0" x2="1" y2="1"><stop offset="0" stop-color="#0a5aa3"/><stop offset="1" stop-color="#9fb7cf"/></linearGradient>
      <linearGradient id="room" x1="0" y1="0" x2="1" y2="1"><stop offset="0" stop-color="#e7e3dc"/><stop offset=".5" stop-color="#b6ad9f"/><stop offset="1" stop-color="#6e6a63"/></linearGradient>
      <linearGradient id="meet" x1="0" y1="0" x2="1" y2="1"><stop offset="0" stop-color="#c9c4bc"/><stop offset="1" stop-color="#5b5148"/></linearGradient>
      <linearGradient id="house" x1="0" y1="0" x2="0" y2="1"><stop offset="0" stop-color="#7d8fc0"/><stop offset=".6" stop-color="#b8a9a6"/><stop offset="1" stop-color="#5e6b46"/></linearGradient>
    </defs>
    <polygon points="893,800 1051,891 1051,1073 893,1164 735,1073 735,891" fill="url(#ring)" stroke="url(#ring)" stroke-width="30" stroke-linejoin="round"/>
    <polygon role="img" aria-label="Photo of a young man relaxing with a laptop in a bright shared living room" points="893,818 1036,900 1036,1064 893,1146 750,1064 750,900" fill="url(#room)" stroke="url(#room)" stroke-width="14" stroke-linejoin="round"/>
    <polygon role="img" aria-label="Photo of housemates chatting at a table" points="1038,746 1084,772 1084,824 1038,850 992,824 992,772" fill="url(#meet)" stroke="url(#meet)" stroke-width="10" stroke-linejoin="round"/>
    <polygon role="img" aria-label="Photo of a suburban house at dusk" points="662,966 708,992 708,1044 662,1070 616,1044 616,992" fill="url(#house)" stroke="url(#house)" stroke-width="10" stroke-linejoin="round"/>
  </svg>
</section>

<!-- PROPERTIES -->
<section>
  <span class="badge center" style="left:600px;top:1193px">Co-Living Spaces</span>
  <h2 class="h2 center" style="top:1228px;font-size:38px">Co-Living Proprties</h2>

  <div class="card" style="left:161px;top:1322px"><div class="photo" role="img" aria-label="Photo of an A-frame cottage at sunset" style="background:linear-gradient(160deg,#b9c3c8,#c77a52 55%,#5a3b2c)"></div><div class="label"><b>Property Name 1</b><span>Location Name</span></div></div>
  <div class="card" style="left:461px;top:1322px"><div class="photo" role="img" aria-label="Photo of a dim lounge with sofas" style="background:linear-gradient(160deg,#3d3128,#8c7b69 55%,#2a221c)"></div><div class="label"><b>Property Name 2</b><span>Location Name</span></div></div>
  <div class="card" style="left:762px;top:1322px"><div class="photo" role="img" aria-label="Photo of a curved modern apartment tower" style="background:linear-gradient(150deg,#3b7fc4,#2c3b55 45%,#b06a32 75%,#1d2738)"></div><div class="label"><b>Property Name 3</b><span>Location Name</span></div></div>
  <div class="card" style="left:161px;top:1614px"><div class="photo" role="img" aria-label="Photo of an orange apartment facade with windows" style="background:linear-gradient(150deg,#e08c2f,#c36e1f 55%,#2f4a55)"></div><div class="label"><b>Property Name 4</b><span>Location Name</span></div></div>
  <div class="card" style="left:461px;top:1614px"><div class="photo" role="img" aria-label="Photo of a family house under a pink sky" style="background:linear-gradient(180deg,#e48aa0,#b89a90 50%,#4f6e36)"></div><div class="label"><b>Property Name 5</b><span>Location Name</span></div></div>
  <div class="card" style="left:762px;top:1614px"><div class="photo" role="img" aria-label="Photo of a white residence courtyard with garden" style="background:linear-gradient(180deg,#6ea3d6,#dfe3e6 45%,#5d7a44)"></div><div class="label"><b>Property Name 6</b><span>Location Name</span></div></div>

  <a class="btn btn-outline" style="left:468px;top:1941px;width:128px;height:37px">All Properties</a>
  <a class="btn" style="left:611px;top:1941px;width:119px;height:37px;font-weight:500">Inquiry Now</a>
</section>

<!-- PARTNERS -->
<section>
  <div class="abs partners"></div>
  <span class="badge center" style="left:600px;top:2099px">Co-Living Spaces</span>
  <h2 class="h2 center" style="top:2134px;font-size:38px">Co-Living Partners</h2>
  <div class="p-card" style="left:161px"><h3>Developers</h3><p>Lorem Ipsum is simply dummy text of the printing and typesetting industry. Lorem Ipsum has been the industry's standard dummy text ever since the 1500s, when an unknown printer took a galley of type and scrambled it to make a type specimen book.</p></div>
  <div class="p-card" style="left:611px"><h3>Investors</h3><p>Lorem Ipsum is simply dummy text of the printing and typesetting industry. Lorem Ipsum has been the industry's standard dummy text ever since the 1500s, when an unknown printer took a galley of type and scrambled it to make a type specimen book.</p></div>
  <svg class="abs" style="left:320px;top:2195px" width="600" height="100" viewBox="320 2195 600 100">
    <polygon points="374,2205 405,2223 405,2263 374,2281 343,2263 343,2223" fill="#0a5aa3" stroke="#0a5aa3" stroke-width="8" stroke-linejoin="round"/>
    <path d="M360 2258H388M366 2258V2240L374 2232L382 2240V2258" fill="none" stroke="#cfe2f5" stroke-width="2"/>
    <polygon points="825,2205 856,2223 856,2263 825,2281 794,2263 794,2223" fill="#0a5aa3" stroke="#0a5aa3" stroke-width="8" stroke-linejoin="round"/>
    <circle cx="825" cy="2236" r="9" fill="none" stroke="#cfe2f5" stroke-width="2"/>
    <path d="M809 2256C815 2250 822 2252 828 2254H840" fill="none" stroke="#cfe2f5" stroke-width="2"/>
  </svg>
  <a class="btn" style="left:547px;top:2470px;width:105px;height:37px;font-size:15px">Let's Talk</a>
</section>

<!-- CALL TO ACTION BAND -->
<section>
  <div class="abs band"></div>
  <span class="badge light center" style="left:600px;top:2620px;border:1px solid #ccc">Co-Living Spaces</span>
  <h2 class="abs band-title">Want To Start A Home?</h2>
  <p class="abs band-copy">Lorem Ipsum is simply dummy text of the printing and typesetting industry. Lorem Ipsum has been the industry's standard dummy text ever since the 1500s, when an unknown printer took a galley of type and scrambled it to make a type specimen book.</p>
  <a class="btn btn-white" style="left:529px;top:2797px;width:142px;height:35px;font-size:15px">Find Your Home</a>
</section>

<!-- PHOTO FEED -->
<section>
  <span class="badge center" style="left:600px;top:2966px">Co-Living Spaces</span>
  <h2 class="h2 center" style="top:3002px;font-size:40px">View Our Photo Feeds</h2>
  <div class="tile" style="left:161px;top:3076px;background:linear-gradient(160deg,#dedbd3,#8a877c 60%,#3d3b35)" role="img" aria-label="Photo of friends in a bright living room"></div>
  <div class="tile" style="left:386px;top:3076px;background:linear-gradient(160deg,#3d3128,#8c7b69 55%,#2a221c)" role="img" aria-label="Photo of a lounge with sofas"></div>
  <div class="tile" style="left:611px;top:3076px;background:linear-gradient(160deg,#eaf1f5,#7fb3c7 50%,#2f6f86)" role="img" aria-label="Photo of a glass tower from below"></div>
  <div class="tile" style="left:837px;top:3076px;background:linear-gradient(180deg,#e9e6e1,#c9b9a6 60%,#7a6b5e)" role="img" aria-label="Photo of a young woman sitting on a sofa with a guitar"></div>
  <div class="tile" style="left:161px;top:3301px;background:linear-gradient(180deg,#e8e2d8,#9d907d 60%,#5a4b3c)" role="img" aria-label="Photo of a cosy living room with sofa"></div>
  <div class="tile" style="left:386px;top:3301px;background:linear-gradient(180deg,#ece9e4,#a19a91 55%,#6a5440)" role="img" aria-label="Photo of people working on laptops together"></div>
  <div class="tile" style="left:611px;top:3301px;background:linear-gradient(160deg,#b6a58e,#6d6a50 55%,#3c3a2f)" role="img" aria-label="Photo of a woman laughing with friends"></div>
  <div class="tile" style="left:837px;top:3301px;background:linear-gradient(180deg,#e4e1dc,#7e6e62 55%,#2c2624)" role="img" aria-label="Photo of friends sharing a meal"></div>
  <a class="btn" style="left:503px;top:3560px;width:194px;height:37px;font-size:15px">Follow Our Photo Feed</a>
</section>

<!-- WHY US -->
<section>
  <svg class="abs" style="left:100px;top:3610px" width="520" height="450" viewBox="100 3610 520 450">
    <defs>
      <linearGradient id="ring2" x1="0" y1="0" x2="1" y2="1"><stop offset="0" stop-color="#0a5aa3"/><stop offset="1" stop-color="#8fa6bd"/></linearGradient>
      <linearGradient id="tower" x1="0" y1="0" x2="1" y2="1"><stop offset="0" stop-color="#4a8fd6"/><stop offset=".45" stop-color="#2b3a55"/><stop offset=".7" stop-color="#b06a32"/><stop offset="1" stop-color="#1d2738"/></linearGradient>
      <linearGradient id="lounge" x1="0" y1="0" x2="0" y2="1"><stop offset="0" stop-color="#ece6dc"/><stop offset="1" stop-color="#6d5b48"/></linearGradient>
      <linearGradient id="work" x1="0" y1="0" x2="1" y2="1"><stop offset="0" stop-color="#f1ede6"/><stop offset="1" stop-color="#b37a3c"/></linearGradient>
    </defs>
    <polygon points="306,3684 464,3775 464,3957 306,4048 148,3957 148,3775" fill="url(#ring2)" stroke="url(#ring2)" stroke-width="30" stroke-linejoin="round"/>
    <polygon role="img" aria-label="Photo of a curved modern apartment tower against blue sky" points="306,3702 449,3784 449,3948 306,4030 163,3948 163,3784" fill="url(#tower)" stroke="url(#tower)" stroke-width="14" stroke-linejoin="round"/>
    <polygon role="img" aria-label="Photo of a furnished shared lounge" points="162,3630 208,3656 208,3708 162,3734 116,3708 116,3656" fill="url(#lounge)" stroke="url(#lounge)" stroke-width="10" stroke-linejoin="round"/>
    <polygon role="img" aria-label="Photo of housemates working at a table" points="535,3849 581,3875 581,3927 535,3953 489,3927 489,3875" fill="url(#work)" stroke="url(#work)" stroke-width="10" stroke-linejoin="round"/>
  </svg>
  <span class="badge" style="left:613px;top:3676px">Co-Living Spaces</span>
  <h2 class="h2" style="left:613px;top:3712px">Why Us?</h2>
  <p class="copy" style="left:613px;top:3776px;width:428px">Lorem Ipsum is simply dummy text of the printing and typesetting industry. Lorem Ipsum has been the industry's standard dummy text ever since the 1500s, when an unknown printer took a galley of type and scrambled it to make a type specimen book.</p>
  <p class="copy" style="left:613px;top:3876px;width:428px">&nbsp;It was popularised in the 1960s with the release of transfer sheets containing Lorem Ipsum passages, and more recently with desktop publishing software and page layout tools including versions of Lorem Ipsum.</p>
  <a class="btn" style="left:611px;top:3978px;width:119px;height:35px;font-size:15px">Explore More</a>
</section>

<!-- PRESS -->
<section aria-label="Featured in">
  <div class="press" style="left:161px"><i></i></div>
  <div class="press" style="left:341px"><i></i></div>
  <div class="press" style="left:521px"><i></i></div>
  <div class="press" style="left:700px"><i></i></div>
  <div class="press" style="left:880px"><i></i></div>
  <span class="dot" style="left:560px"></span>
  <span class="dot" style="left:585px;background:var(--blue)"></span>
  <span class="dot" style="left:607px"></span>
  <span class="dot" style="left:630px"></span>
</section>

<!-- FOOTER -->
<footer class="abs footer">
  <svg class="abs" style="left:0;top:0" width="300" height="249" viewBox="0 0 300 249"><path d="M0 60C60 30 120 40 170 70C230 105 250 170 260 249H0Z" fill="#ffffff" opacity=".05"/></svg>
  <div class="abs foot-logo">HEARTHSIDE</div>
  <span class="abs foot-link" style="left:349px">Home</span>
  <span class="abs foot-link" style="left:446px">Properties</span>
  <span class="abs foot-link" style="left:571px">About Us</span>
  <span class="abs foot-link" style="left:688px">Partner</span>
  <span class="abs foot-link" style="left:776px">Contact Us</span>
  <span class="abs social" style="left:495px" aria-label="Social link"></span>
  <span class="abs social" style="left:539px" aria-label="Social link"></span>
  <span class="abs social" style="left:584px" aria-label="Social link"></span>
  <span class="abs social" style="left:630px" aria-label="Social link"></span>
  <span class="abs social" style="left:673px" aria-label="Social link"></span>
  <p class="abs legal">Copyright © 2019 - Co - Living. All Rights Reserved.</p>
</footer>

</body>
</html>
```